GKRB-Postcard

We need a postcard design of a book. The card will be mailed out by Holbar Press to church leaders. Attached, please find a photo of the book cover, Word doc. with the message that should placed on the card, and a pre-designed sample. You may use a similar layout as the PDF sample or something more attractive. If you can, copy the publisher's logo and book information from the PDF file. Thank you.

Industry/Entity Type

Church

```html
<!DOCTYPE html>
<html lang="en">
<head>
<meta charset="utf-8">
<title>GKRB Postcard</title>
<link rel="stylesheet" href="https://fonts.googleapis.com/css2?family=Questrial&family=Roboto+Slab:wght@800&family=Libre+Baskerville:wght@700&display=swap">
<style>
  :root {
    --stage: #b6c2c2;
    --ink: #111111;
    --night: #050505;
    --paper: #ffffff;
    --deep-red: #c8161d;
    --band: #b9b9b9;
    --body: #333333;
    --muted: #555555;
  }
  * { box-sizing: border-box; margin: 0; padding: 0; }
  html, body { width: 1200px; height: 1000px; overflow: hidden; }
  body {
    position: relative;
    background: var(--stage);
    font-family: "Questrial", "Century Gothic", sans-serif;
    color: var(--ink);
  }

  /* ---------- Book cover ---------- */
  .cover {
    position: absolute;
    left: 62px; top: 201px;
    width: 452px; height: 583px;
    background: var(--night);
    overflow: hidden;
  }
  .cover-art {
    position: absolute;
    left: 0; top: 40px;
    width: 452px; height: 543px;
    background:
      radial-gradient(ellipse 44% 34% at 50% 27%, #8d6a55 0%, #5a4030 45%, rgba(20,14,10,0) 100%),
      radial-gradient(circle at 48% 74%, #3d6a94 0%, #1f3f63 38%, #0c1a2c 60%, rgba(5,5,5,0) 72%);
  }
  .cover-author {
    position: absolute;
    top: 34px; left: 0; width: 100%;
    text-align: center;
    color: var(--paper);
    font-size: 13px;
    letter-spacing: 14px;
    padding-left: 14px;
  }
  .cover-title {
    position: absolute;
    left: 75px; top: 410px;
    width: 360px;
    color: var(--paper);
    font-weight: 400;
    line-height: 1;
  }
  .cover-title .main {
    display: block;
    font-size: 62px;
    letter-spacing: 1px;
  }
  .cover-title .sub {
    display: block;
    font-size: 36px;
    margin-top: 22px;
  }

  /* ---------- Postcard ---------- */
  .postcard {
    position: absolute;
    left: 552px; top: 267px;
    width: 583px; height: 451px;
    background: var(--paper);
    overflow: hidden;
  }
  .card-band {
    position: absolute;
    left: 0; top: 151px;
    width: 100%; height: 105px;
    background: var(--band);
  }
  .card-band-art {
    position: absolute;
    left: 100px; top: 0;
    width: 483px; height: 105px;
    background: linear-gradient(90deg, rgba(185,185,185,0) 0%, #cfcfcf 30%, #e6e6e6 55%, #c9c9c9 75%, #d8d8d8 100%);
  }
  .card-divider {
    position: absolute;
    left: 278px; top: 43px;
    width: 2px; height: 376px;
    background: var(--ink);
  }
  .card-title {
    position: absolute;
    left: 76px; top: 48px;
    width: 196px;
    color: var(--ink);
    font-weight: 400;
    line-height: 1;
  }
  .card-title .main { display: block; font-size: 30px; }
  .card-title .sub { display: block; font-size: 18px; margin-top: 6px; }
  .card-author {
    position: absolute;
    left: 78px; top: 120px;
    font-size: 13px;
    letter-spacing: 3.5px;
  }
  .card-hook {
    position: absolute;
    left: 22px; top: 160px;
    width: 245px;
    font-family: "Roboto Slab", "Rockwell", serif;
    font-weight: 800;
    font-size: 9.6px;
    line-height: 1.2;
    color: var(--deep-red);
  }
  .card-body {
    position: absolute;
    left: 22px; top: 264px;
    width: 246px;
    font-size: 8.3px;
    line-height: 1.3;
    color: var(--body);
  }
  .card-body p + p { margin-top: 7px; }
  .card-body em { font-style: italic; color: var(--ink); }
  .card-order {
    position: absolute;
    right: 25px; top: 262px;
    width: 260px;
    text-align: right;
  }
  .card-order .availability {
    font-family: "Libre Baskerville", Georgia, serif;
    font-weight: 700;
    font-size: 9.4px;
    line-height: 1.35;
    color: var(--deep-red);
  }
  .card-order .where {
    margin-top: 8px;
    font-size: 8.4px;
    line-height: 1.3;
    color: var(--muted);
  }
  .card-order .isbns {
    margin-top: 9px;
    list-style: none;
    font-size: 8.4px;
    line-height: 1.3;
    color: var(--muted);
  }
  .publisher {
    margin-top: 10px;
    display: flex;
    justify-content: flex-end;
    align-items: center;
    gap: 5px;
    font-family: "Libre Baskerville", Georgia, serif;
    font-weight: 700;
    font-size: 15px;
    color: var(--ink);
  }
  .publisher .mark {
    width: 8px; height: 8px;
    background: var(--ink);
    border-radius: 50%;
  }
</style>
</head>
<body>

  <section class="cover">
    <div class="cover-art" role="img" aria-label="Photograph of a hooded man above planet Earth"></div>
    <p class="cover-author">PAUL EVERARD</p>
    <h1 class="cover-title">
      <span class="main">THE DEVIL</span>
      <span class="sub">in Silent Eden</span>
    </h1>
  </section>

  <section class="postcard">
    <div class="card-band">
      <div class="card-band-art" role="img" aria-label="Greyscale photograph of a hooded man"></div>
    </div>
    <div class="card-divider"></div>

    <h2 class="card-title">
      <span class="main">THE DEVIL</span>
      <span class="sub">in Silent Eden</span>
    </h2>
    <p class="card-author">PAUL EVERARD</p>

    <p class="card-hook">There is a ferocious enemy in our world that's wreaking havoc in human culture. his name is Satan (the Devil), but millions of people don't believe that he exists.</p>

    <div class="card-body">
      <p>Despite the widespread preaching of the gospel, only 4 in 10 (40%) American Christians believe the Satan exist. Those who believe think of him not as a real being but only as a symbol of evil.</p>
      <p>Satan is not only real but deeply entrenched in modern societies harming us in ways that we can't possibly imagine.</p>
      <p>Discover how he influences people daily, regardless of their religious beliefs, for his purpose.</p>
      <p><em>The Devil in Silent Eden</em> not only exposes Satan's diabolical schemes in our world, but also shows how you can defend yourself against the most dangerous and aggressive personality in the universe and make it to heaven safely.</p>
    </div>

    <div class="card-order">
      <p class="availability">Available now from Holbar Press<br>www.holbarpress.com</p>
      <p class="where">Order this title through your local bookseller<br>or preferred on-line retailer.</p>
      <ul class="isbns">
        <li>978-1-5550-1201-3 (SC ISBN)</li>
        <li>978-1-5550-1202-0 (HC ISBN)</li>
        <li>978-1-5550-1200-6 (Ebook ISBN)</li>
      </ul>
      <div class="publisher"><span class="mark"></span><span>Holbar Press</span></div>
    </div>
  </section>

</body>
</html>
```